KO-TRA , Artificial hedge flyer

i need new flyer, in att i'm sending old one but as we produce artificial flowers, trees and most popular is artificial green hedge, and it's used from variety places, from swimming pool, restaurants, bars, private terrace, gardens, to protect from neighbor :-) . from beginning is all our product, it's not imported from other producer. we are doing it by measure what we get from customer ( tailor made ) , we give guaranty 15-20 years on all weather that will not loos color, etc.. you can see some pictures in att on old flyer, and some new pictures of same in space newly added. we'd like more pictures with samples of use, etc.you can see our product on www.ko-tra.hr so you can closely known what we are producing, and what for we need new flyer. we have plenty of new picture that are not on our web, so i can use it for new flyer.

Font styles to use
Sans Serif

Requirements
Must have
• company logo, contact info ( sent in word document in att ), logo of croatian product ( on old flyer in att on front side), stamp Quality since 1950 if you could change year to 1960, last time they made mistake and write 1950 ),
Nice to have
• flyer 3 fold type, or if you think it will look better only double side flyer, depend of design and theme so everyone can understand what is our business

```html
<!DOCTYPE html>
<html lang="hr">
<head>
<meta charset="utf-8">
<title>KO-TRA d.o.o. – Trifold flyer</title>
<link href="https://fonts.googleapis.com/css2?family=Montserrat:wght@500;700&display=swap" rel="stylesheet">
<style>
  :root {
    --stage: #bdbdbc;
    --green-deep: #3c7a12;
    --green-base: #478c19;
    --green-light: #7cc242;
    --green-bright: #22a31a;
    --logo-green: #8fd14f;
    --hedge-dark: #24491a;
    --hedge-mid: #3d6e27;
    --ink-light: #ffffff;
    --ink-yellow: #e6f24a;
  }
  * { margin: 0; padding: 0; box-sizing: border-box; }
  html, body { width: 1200px; height: 2396px; overflow: hidden; }
  body {
    background: var(--stage);
    font-family: "Montserrat", Arial, sans-serif;
    color: var(--ink-light);
    position: relative;
  }
  .spread {
    position: absolute;
    left: 60px;
    width: 1080px;
    height: 764px;
    background: var(--green-base);
    overflow: hidden;
    box-shadow: 0 10px 30px rgba(0,0,0,0.25);
  }
  .spread--outside { top: 334px; }
  .spread--inside { top: 1298px; }
  .spread svg.artwork { position: absolute; inset: 0; width: 1080px; height: 764px; }
  .logo {
    position: absolute;
    display: flex;
    align-items: center;
    gap: 10px;
    font-weight: 500;
    font-size: 34px;
    color: var(--logo-green);
    letter-spacing: 0.5px;
  }
  .logo__dot { width: 28px; height: 28px; border-radius: 50%; background: var(--logo-green); }
  .contact { position: absolute; font-size: 15px; line-height: 1.35; }
  .contact__title { font-weight: 700; font-size: 16px; margin-bottom: 8px; letter-spacing: 0.3px; }
  .contact__row { display: flex; align-items: flex-start; gap: 8px; }
  .contact__row svg { flex: none; margin-top: 3px; }
  .contact__gap { height: 8px; }
  .about { position: absolute; left: 40px; top: 120px; width: 290px; }
  .about__title { font-weight: 700; font-size: 18px; color: var(--ink-yellow); margin-bottom: 12px; }
  .about__text { font-size: 14px; line-height: 1.4; color: var(--ink-yellow); }
</style>
</head>
<body>

<section class="spread spread--outside">
  <svg class="artwork" viewBox="0 0 1080 764" xmlns="http://www.w3.org/2000/svg">
    <defs>
      <linearGradient id="hedgeTone" x1="0" y1="0" x2="1" y2="1">
        <stop offset="0" stop-color="var(--hedge-mid)"/>
        <stop offset="1" stop-color="var(--hedge-dark)"/>
      </linearGradient>
      <linearGradient id="terraceTone" x1="0" y1="0" x2="1" y2="1">
        <stop offset="0" stop-color="#6f8f55"/>
        <stop offset="0.6" stop-color="#8a8a7c"/>
        <stop offset="1" stop-color="#4d7a35"/>
      </linearGradient>
    </defs>
    <path d="M0,0 L430,0 C390,130 300,220 190,270 C120,300 60,310 0,300 Z" fill="url(#terraceTone)" role="img" aria-label="Photo: terrace with lounger and umbrella in front of an artificial hedge"/>
    <path d="M0,300 C60,310 120,300 190,270 C300,220 390,130 430,0" fill="none" stroke="var(--green-light)" stroke-width="14"/>
    <path d="M40,340 C220,560 540,460 720,300 C860,180 1000,200 1060,190 L1060,630 C900,700 700,740 520,764 L70,764 C50,620 40,480 40,340 Z" fill="url(#hedgeTone)" role="img" aria-label="Photo: tall artificial green hedge with trees behind"/>
    <path d="M20,330 C200,580 540,480 720,300 C860,170 1000,185 1080,172" fill="none" stroke="var(--green-light)" stroke-width="22"/>
    <path d="M70,764 C45,620 35,480 40,340" fill="none" stroke="var(--green-light)" stroke-width="14"/>
    <path d="M520,764 C700,740 900,700 1080,610" fill="none" stroke="var(--green-light)" stroke-width="16"/>
    <line x1="360" y1="0" x2="360" y2="764" stroke="#000" stroke-opacity="0.08" stroke-width="2"/>
    <line x1="720" y1="0" x2="720" y2="764" stroke="#000" stroke-opacity="0.08" stroke-width="2"/>
  </svg>

  <div class="contact" style="left:400px; top:110px;">
    <div class="contact__title">CONTACT US:</div>
    <div class="contact__row">
      <svg width="12" height="14" viewBox="0 0 12 14"><path d="M6 0a5 5 0 0 1 5 5c0 4-5 9-5 9S1 9 1 5a5 5 0 0 1 5-5z" fill="#fff"/><circle cx="6" cy="5" r="2" fill="var(--green-base)"/></svg>
      <span>Lipova ulica 8, BREZJE<br>10432 SV. Martin</span>
    </div>
    <div class="contact__row">
      <svg width="12" height="12" viewBox="0 0 12 12"><path d="M2 0l2 3-1 1.5c1 2 2.5 3.5 4.5 4.5L9 8l3 2-1 2C5 12 0 7 0 1z" fill="#fff"/></svg>
      <span>+385 98 000 111<br>+385 99 000 22 33</span>
    </div>
    <div class="contact__gap"></div>
    <div class="contact__row">
      <svg width="12" height="12" viewBox="0 0 12 12"><circle cx="6" cy="6" r="5" fill="none" stroke="#fff"/><path d="M1 6h10M6 1c-3 3-3 7 0 10M6 1c3 3 3 7 0 10" fill="none" stroke="#fff"/></svg>
      <span>www.ko-tra.hr</span>
    </div>
    <div class="contact__row">
      <svg width="12" height="10" viewBox="0 0 12 10"><rect x="0.5" y="0.5" width="11" height="9" fill="none" stroke="#fff"/><path d="M0.5 0.5l5.5 5 5.5-5" fill="none" stroke="#fff"/></svg>
      <span>info@ko-tra.hr</span>
    </div>
  </div>

  <div class="logo" style="left:760px; top:40px;"><span class="logo__dot"></span>KO-TRA d.o.o.</div>
</section>

<section class="spread spread--inside">
  <svg class="artwork" viewBox="0 0 1080 764" xmlns="http://www.w3.org/2000/svg">
    <defs>
      <linearGradient id="gardenTone" x1="0" y1="0" x2="0" y2="1">
        <stop offset="0" stop-color="#9fb4a8"/>
        <stop offset="0.45" stop-color="#4f7a34"/>
        <stop offset="1" stop-color="#2f5a22"/>
      </linearGradient>
      <linearGradient id="cafeTone" x1="0" y1="0" x2="1" y2="1">
        <stop offset="0" stop-color="#c9b79c"/>
        <stop offset="1" stop-color="#4a4a44"/>
      </linearGradient>
      <radialGradient id="ballTone" cx="0.4" cy="0.35" r="0.7">
        <stop offset="0" stop-color="#4f8a30"/>
        <stop offset="1" stop-color="#1f4016"/>
      </radialGradient>
      <polygon id="hex" points="80,0 40,69.3 -40,69.3 -80,0 -40,-69.3 40,-69.3"/>
    </defs>

    <path d="M470,0 L1080,0 L1080,230 C1050,330 990,400 920,430 L470,430 Z" fill="url(#gardenTone)" role="img" aria-label="Photo: garden with artificial hedge, trees and a house behind"/>
    <path d="M1080,230 C1050,330 990,400 920,430" fill="none" stroke="var(--green-light)" stroke-width="14"/>
    <path d="M0,420 L250,380 L270,764 L0,764 Z" fill="url(#cafeTone)" role="img" aria-label="Photo: café terrace with artificial green wall and chairs"/>

    <g stroke="var(--green-bright)" stroke-width="10" stroke-linejoin="round">
      <use href="#hex" x="250" y="436" fill="#5f8f3a" role="img" aria-label="Photo: green wall at a café entrance"/>
      <use href="#hex" x="250" y="575" fill="#7aa84c" role="img" aria-label="Photo: hedge panel close up"/>
      <use href="#hex" x="370" y="367" fill="#8a5a3c" role="img" aria-label="Photo: hedge beside a building"/>
      <use href="#hex" x="370" y="505" fill="#6f9e3f" role="img" aria-label="Photo: artificial hedge wall close up"/>
      <use href="#hex" x="370" y="644" fill="#5a7e44" role="img" aria-label="Photo: hedge along a terrace"/>
      <use href="#hex" x="490" y="160" fill="#6e9a48" role="img" aria-label="Photo: hedge on a rooftop"/>
      <use href="#hex" x="490" y="298" fill="#4d6e38" role="img" aria-label="Photo: hedge around a courtyard"/>
      <use href="#hex" x="490" y="436" fill="#5c7f4a" role="img" aria-label="Photo: terrace with hedge and pergola"/>
      <use href="#hex" x="490" y="575" fill="#8c9a84" role="img" aria-label="Photo: hedge along a driveway"/>
      <use href="#hex" x="610" y="367" fill="#9c7a5e" role="img" aria-label="Photo: terrace seating with flowers and hedge"/>
      <use href="#hex" x="610" y="505" fill="#6a8d52" role="img" aria-label="Photo: hedge screening a garden"/>
    </g>

    <circle cx="860" cy="270" r="95" fill="url(#ballTone)" role="img" aria-label="Photo: artificial boxwood ball"/>

    <path d="M330,764 C600,720 900,700 1080,620 L1080,764 Z" fill="var(--green-deep)"/>
    <path d="M330,764 C600,720 900,700 1080,620" fill="none" stroke="var(--green-light)" stroke-width="18"/>
    <line x1="360" y1="0" x2="360" y2="764" stroke="#000" stroke-opacity="0.08" stroke-width="2"/>
    <line x1="720" y1="0" x2="720" y2="764" stroke="#000" stroke-opacity="0.08" stroke-width="2"/>
  </svg>

  <div class="logo" style="left:40px; top:40px;"><span class="logo__dot"></span>KO-TRA d.o.o.</div>

  <div class="about">
    <div class="about__title">WHAT WE DO:</div>
    <p class="about__text">Unutarnje i vanjsko uređenje poslovnih, stambenih, sportskih i ostalih prostora umjetnom živicom, dekorativnim cvijećem, drvećem i aranžmanima</p>
  </div>

  <div class="contact" style="left:790px; top:470px;">
    <div class="contact__title">CONTACT US:</div>
    <div class="contact__row">
      <svg width="12" height="14" viewBox="0 0 12 14"><path d="M6 0a5 5 0 0 1 5 5c0 4-5 9-5 9S1 9 1 5a5 5 0 0 1 5-5z" fill="#fff"/><circle cx="6" cy="5" r="2" fill="var(--green-base)"/></svg>
      <span>Lipova ulica 8, BREZJE<br>10432 SV. Martin</span>
    </div>
    <div class="contact__row">
      <svg width="12" height="12" viewBox="0 0 12 12"><path d="M2 0l2 3-1 1.5c1 2 2.5 3.5 4.5 4.5L9 8l3 2-1 2C5 12 0 7 0 1z" fill="#fff"/></svg>
      <span>+385 98 000 111<br>+385 99 000 22 33</span>
    </div>
    <div class="contact__row">
      <svg width="12" height="12" viewBox="0 0 12 12"><circle cx="6" cy="6" r="5" fill="none" stroke="#fff"/><path d="M1 6h10M6 1c-3 3-3 7 0 10M6 1c3 3 3 7 0 10" fill="none" stroke="#fff"/></svg>
      <span>www.ko-tra.hr</span>
    </div>
    <div class="contact__row">
      <svg width="12" height="10" viewBox="0 0 12 10"><rect x="0.5" y="0.5" width="11" height="9" fill="none" stroke="#fff"/><path d="M0.5 0.5l5.5 5 5.5-5" fill="none" stroke="#fff"/></svg>
      <span>info@ko-tra.hr</span>
    </div>
  </div>
</section>

</body>
</html>
```